Set of banners for Strollvia.com

We are Strollvia.com, an international online shop focussing on prams and buggies, selling all over the world.
We are changing our homepage banner to a changing set of banners which you can click through. (attachment: current banner), as example for changing set of banners: www.plenkobox.com.
Positioning
Our main advantage is that we have a huge range of upscale international brands of prams, which are not available in many of our target countries. That is why we want to use the slogan "Global Strollers for Unique Parents"
Our banner have always a text and in the lower half or at the bottom a button (attachment: current banner with button, or from another site see attachment: button-learn-more)
There should be four banners
a) Global Strollers for Unique Parents
this will be our main banner and will used for our facebook and youtube channel as well. Some ideas
- similar to current facebook (attachment: current facebook)
- many prams in background + title (attachment: many prams)
The text is "Global Strollers for Unique Parents"
Below: See all Prams (Button)
b) Strollvia.com Bonus - Get 2 % Back
this is our rewards program. Customers get 2 % rewards on very purchase which they can use for a future purchase
- as an example a banner for a rewards programm of kuschelo.de a german site (attachment rewards-kuschelode)
The text is
Title: Strollvia.com Bonus
Text: Get 2 % back on every purchase
Below: Learn more (Button)
c) Special Offers - save up to 50 %
This is our Special offers banner, it links to our special offers category
http://www.strollvia.com/offers/?inref=home-banner&order=price&dir=desc
Text: Special Offers - save up to 50 %
Below: Save Now (Button)
d) New Products at Strollvia.com
This links to our "new products" page
http://www.strollvia.com/new-products?np=true
Text: New Products at Strollvia.com
Below: See new Products (Button)
Target Market(s)
mothers, young families
Industry/Entity Type
Shop
Font styles to use
Other font styles liked:
- like used on www.strollvia.com
Look and feel
Each slider illustrates characteristics of the customer's brand and the style your logo design should communicate.

```html
<!DOCTYPE html>
<html lang="en">
<head>
<meta charset="utf-8">
<title>Strollvia.com Bonus – Get 2% back</title>
<link href="https://fonts.googleapis.com/css2?family=Arimo:wght@400;700&display=swap" rel="stylesheet">
<style>
  :root {
    --plum: #5a1f4f;
    --sun: #f7ec3a;
    --sky: #bcd8ea;
    --mist: #d9e9f0;
    --cream: #eef0d4;
    --navy: #1d4660;
    --navy-edge: #2f6a86;
    --white: #ffffff;
  }
  * { margin: 0; padding: 0; box-sizing: border-box; }
  html, body { width: 1200px; height: 358px; overflow: hidden; background: var(--white); }
  .banner {
    position: relative;
    width: 1200px;
    height: 358px;
    overflow: hidden;
    font-family: "Arimo", Arial, sans-serif;
  }
  .backdrop {
    position: absolute;
    inset: 0;
    background: linear-gradient(to bottom, var(--mist) 0%, var(--sky) 45%, var(--cream) 85%);
  }
  .ground-band {
    position: absolute;
    left: 0;
    bottom: 0;
    width: 1200px;
    height: 52px;
    background: var(--sun);
  }
  .pram-art {
    position: absolute;
    left: 84px;
    top: 22px;
    width: 420px;
    height: 324px;
    border-radius: 24px;
    background: linear-gradient(160deg, rgba(29,70,96,0.22), rgba(29,70,96,0.10));
  }
  .corner-ribbon { position: absolute; left: 0; top: 0; width: 210px; height: 210px; }
  .corner-ribbon__text {
    position: absolute;
    left: -4px;
    top: 46px;
    width: 170px;
    transform: rotate(-45deg);
    text-align: center;
    font-weight: 700;
    line-height: 1;
  }
  .corner-ribbon__name { display: block; color: var(--sun); font-size: 21px; }
  .corner-ribbon__label { display: block; color: var(--white); font-size: 33px; margin-top: 2px; }
  .offer-badge {
    position: absolute;
    left: 845px;
    top: 10px;
    width: 300px;
    height: 300px;
    border-radius: 50%;
    background: var(--plum);
    color: var(--white);
    text-align: center;
    font-weight: 700;
    padding-top: 60px;
  }
  .offer-badge__get { font-size: 40px; line-height: 1; }
  .offer-badge__rate { font-size: 106px; line-height: 0.95; color: var(--sun); letter-spacing: -2px; }
  .offer-badge__small { font-size: 23px; line-height: 1.1; margin-top: 6px; }
  .offer-badge__big { font-size: 35px; line-height: 1; }
  .cta-button {
    position: absolute;
    left: 524px;
    top: 262px;
    width: 306px;
    height: 74px;
    border-radius: 8px;
    background: var(--navy);
    border: 3px solid var(--navy-edge);
    color: var(--white);
    font-weight: 700;
    font-size: 34px;
    display: flex;
    align-items: center;
    justify-content: center;
    text-decoration: none;
  }
</style>
</head>
<body>
  <main class="banner">
    <div class="backdrop" role="img" aria-label="Soft pastel horizontal stripes in light blue, lilac and cream"></div>
    <div class="ground-band" role="img" aria-label="Wavy yellow border along the bottom edge"></div>

    <div class="pram-art" role="img" aria-label="Line drawing of a baby pram with a hood and large spoked wheels"></div>

    <svg class="corner-ribbon" viewBox="0 0 210 210" aria-hidden="true">
      <polygon points="0,0 210,0 0,210" fill="var(--plum)"/>
    </svg>
    <div class="corner-ribbon__text">
      <span class="corner-ribbon__name">Strollvia.com</span>
      <span class="corner-ribbon__label">Bonus</span>
    </div>

    <div class="offer-badge">
      <div class="offer-badge__get">Get</div>
      <div class="offer-badge__rate">2%</div>
      <div class="offer-badge__small">back on every</div>
      <div class="offer-badge__big">purchase</div>
    </div>

    <a class="cta-button" href="#">Learn More</a>
  </main>
</body>
</html>
```